Facebook page as well as a business card and stationary design for a fitness instructor/personal trainer who is branching out as an independent worker delivering the gym experience (personal training or small group classes) to the home market. The trainer (RP or Rod Pellinger) is young, energetic, and results oriented.

Job Type
Facebook page and 2-sided business card
Task Outline
Create a Facebook presence (supported by a business card) for a train-you-at-home personal trainer
Task Description
Looking for a Graphic Designer/Web Designer to make a really modern/clean Facebook page that promotes Rod Pellinger ("RP") as at-your-home personal trainer. Rod's goal as a personal trainer is to motivate, inspire and educate all of his clients about the benefits of regular exercise, nourishing the body with nutritious foods, and living a healthy lifestyle while enjoying working out. He wants to encourage the convenience component of what he does by offering personal training sessions at a person's home or place of business. He trains both men and women, so the design of both the business card and the Facebook page should appeal to both genders and not come across as more feminine or more masculine. The Facebook page should include links to the Chirper, Instagram, and email accounts. It should also hold a placeholder link to his future web site called BougeAuLogis.

He holds several certifications and would like these mentioned on his Facebook page and perhaps on his business card -- either in text form or identifying them with the logos (which are attached).

Contact information for the business card will be supplied shortly. In the interim, the following can be used: Rod Pellinger Personal Trainer; Address: 287 Vauquelin, Val-Brisé, Laurentie, J4K 7N2, Email: rpstrongdaily@mailbox.example; Phone: 514.302-4519; Facebook: RPStrongDaily; Chirper: RPStrongDaily; Website: BougeAuLogis.example

OTHER INFORMATION: This project is a Christmas present to the personal trainer who is a friend. He'll be making the final decisions on the designs for both components.
Updates

Target Market(s)

Both men and women who don't have the time for the gym and are looking for personal training at home or at their place of work.

Industry/Entity Type

Personal Trainer

Contact Information for Business Card

No photo. Clean lines and preference of blue colouring. contact information presented clearly. Card design must radiate the concept of fitness for life, living healthy and strong.

Font styles to use
Sans Serif

Colors
34a7d8
86cae6
85acd3
0355a3
0592ce
cee9f5
ceddec
86cfc6
cfeae6

```html
<!DOCTYPE html>
<html lang="en">
<head>
<meta charset="utf-8">
<title>Rod Pellinger – Page</title>
<link rel="stylesheet" href="https://fonts.googleapis.com/css2?family=Bebas+Neue&family=Noto+Sans+Bengali:wght@400;700&display=swap">
<style>
  :root {
    --stage: #3b3b3b;
    --cover-dark: #1b1b1d;
    --brand-blue: #0b4a8e;
    --brand-blue-deep: #083a70;
    --ink-light: #f2f2f2;
    --silver: #d9d9d9;
    --fb-grey: #e9eaed;
    --fb-line: #dddfe2;
    --fb-text: #4b4f56;
    --fb-blue: #3b5998;
    --white: #ffffff;
  }
  * { box-sizing: border-box; margin: 0; padding: 0; }
  html, body { width: 1200px; height: 800px; overflow: hidden; background: var(--stage); }
  .page { position: absolute; left: 175px; top: 168px; width: 850px; height: 415px; background: var(--fb-grey); overflow: hidden; }
  .cover { position: absolute; left: 0; top: 0; width: 850px; height: 315px; background: var(--cover-dark); overflow: hidden; }
  .cover-shapes { position: absolute; inset: 0; }
  .name { position: absolute; left: 16px; top: 32px; font: 62px/1 "Bebas Neue", sans-serif; color: var(--silver); letter-spacing: 1px; white-space: nowrap; }
  .tagline { position: absolute; left: 17px; top: 90px; font: 28px/1 "Bebas Neue", sans-serif; color: var(--ink-light); letter-spacing: .5px; white-space: nowrap; }
  .contacts { position: absolute; left: 565px; top: 34px; list-style: none; }
  .contacts li { display: flex; align-items: center; height: 25px; margin-bottom: 3.4px; width: 285px;
    background: linear-gradient(90deg, var(--brand-blue-deep) 0%, rgba(8,58,112,.45) 70%, rgba(8,58,112,0) 100%); }
  .contacts .icon { flex: none; width: 25px; height: 25px; background: var(--brand-blue); display: flex; align-items: center; justify-content: center; }
  .contacts .icon svg { width: 15px; height: 15px; fill: var(--white); }
  .contacts span { margin-left: 8px; font: 13px/1 "Bebas Neue", sans-serif; color: var(--white); letter-spacing: .3px; white-space: nowrap; }
  .cert-band { position: absolute; left: 518px; top: 194px; width: 332px; height: 60px; background: var(--brand-blue); clip-path: polygon(8px 0, 100% 0, 100% 100%, 0 100%); }
  .cert { position: absolute; top: 6px; height: 50px; background: #cfd4da; border: 2px solid var(--white); }
  .actions { position: absolute; top: 275px; display: flex; height: 27px; }
  .btn { display: flex; align-items: center; gap: 5px; height: 27px; padding: 0 9px; background: #f6f7f9; border: 1px solid #ced0d4; font: 13px/1 "Noto Sans Bengali", sans-serif; color: var(--fb-text); white-space: nowrap; }
  .btn svg { width: 12px; height: 12px; fill: var(--fb-text); }
  .profile { position: absolute; left: 14px; top: 175px; width: 168px; height: 167px; background: var(--white); padding: 4px; box-shadow: 0 0 2px rgba(0,0,0,.4); z-index: 2; }
  .profile-mark { width: 100%; height: 100%; background: var(--brand-blue); display: flex; flex-direction: column; justify-content: center; align-items: center; color: var(--white); font-family: "Bebas Neue", sans-serif; }
  .profile-mark .initials { font-size: 86px; line-height: .9; }
  .profile-mark .brand { font-size: 30px; line-height: 1; }
  .nav { position: absolute; left: 0; top: 315px; width: 850px; height: 44px; background: var(--white); border-bottom: 1px solid var(--fb-line); display: flex; align-items: center; padding-left: 196px; }
  .nav a { position: relative; padding: 0 14px; font: 14px/44px "Noto Sans Bengali", sans-serif; color: var(--fb-text); text-decoration: none; }
  .nav a + a::before { content: ""; position: absolute; left: 0; top: 12px; height: 20px; border-left: 1px solid var(--fb-line); }
  .nav a.active { font-weight: 700; color: #1d2129; }
  .nav a.active::after { content: ""; position: absolute; left: 0; right: 0; bottom: 0; height: 3px; background: var(--fb-blue); }
  .card { position: absolute; top: 370px; height: 45px; background: var(--white); border: 1px solid var(--fb-line); display: flex; align-items: center; font: 700 14px/1 "Noto Sans Bengali", sans-serif; color: #4b4f56; }
  .people { left: 0; width: 343px; padding: 0 12px; justify-content: space-between; background: #f6f7f9; }
  .composer { left: 355px; width: 495px; padding: 0 12px; gap: 10px; }
  .composer .tab { display: flex; align-items: center; gap: 6px; }
  .sq { width: 15px; height: 15px; border-radius: 2px; }
</style>
</head>
<body>
<main class="page">
  <section class="cover">
    <svg class="cover-shapes" width="850" height="315" viewBox="0 0 850 315">
      <defs>
        <linearGradient id="portrait-tone" x1="0" y1="0" x2="0" y2="1">
          <stop offset="0" stop-color="#6e6e6e"/><stop offset=".55" stop-color="#a3a3a3"/><stop offset="1" stop-color="#3a3a3a"/>
        </linearGradient>
      </defs>
      <polygon points="0,227 225,0 595,0 315,315 0,315" fill="var(--brand-blue)"/>
      <rect x="245" y="0" width="285" height="315" fill="url(#portrait-tone)" role="img" aria-label="Black and white portrait photo of Rod Pellinger"/>
    </svg>

    <h1 class="name">Rod Pellinger</h1>
    <p class="tagline">- Your Home Personal Trainer -</p>

    <ul class="contacts">
      <li><div class="icon"><svg viewBox="0 0 16 16"><path d="M8 1 1 7.5h2V15h4v-4h2v4h4V7.5h2z"/></svg></div><span>287 Vauquelin, Val-Brisé, Laurentie, J4K 7N2</span></li>
      <li><div class="icon"><svg viewBox="0 0 16 16"><path d="M1 3h14v10H1zM2 4l6 5 6-5v1L8 10 2 5z" fill-rule="evenodd"/></svg></div><span>rpstrongdaily@mailbox.example</span></li>
      <li><div class="icon"><svg viewBox="0 0 16 16"><path d="M4 1 6.5 4 5 6c1 2 3 4 5 5l2-1.5 3 2.5-1.5 2.5C8 14 2 8 1.5 2.5z"/></svg></div><span>555.302-4519</span></li>
      <li><div class="icon"><svg viewBox="0 0 16 16"><circle cx="8" cy="8" r="5"/></svg></div><span>www.chirper.example/rpstrongdaily</span></li>
      <li><div class="icon"><svg viewBox="0 0 16 16"><path d="M6 10 10 6M7 4.5l1.5-1.5a2.8 2.8 0 0 1 4 4L11 8.5M9 11.5 7.5 13a2.8 2.8 0 0 1-4-4L5 7.5" stroke="#fff" stroke-width="1.8" fill="none"/></svg></div><span>www.bougeaulogis.example</span></li>
    </ul>

    <div class="cert-band">
      <div class="cert" style="left:19px;width:50px"></div>
      <div class="cert" style="left:78px;width:100px"></div>
      <div class="cert" style="left:187px;width:60px"></div>
      <div class="cert" style="left:257px;width:60px"></div>
    </div>

    <div class="actions" style="left:463px">
      <div class="btn"><svg viewBox="0 0 12 12"><path d="M1 5h2v6H1zM4 5l3-4c1 0 1.5.5 1.2 2L8 5h3l-1 6H4z"/></svg>পছন্দকৃত ▾</div>
    </div>
    <div class="actions" style="left:586px">
      <div class="btn"><svg viewBox="0 0 12 12"><path d="M1 6.5 2.2 5.3 4.5 7.6 9.8 2.3 11 3.5 4.5 10z"/></svg>অনুসরণ করছেন</div>
      <div class="btn"><svg viewBox="0 0 12 12"><path d="M1 1h10v7H5l-3 3V8H1z"/></svg>বার্তা</div>
      <div class="btn">•••</div>
    </div>
  </section>

  <div class="profile">
    <div class="profile-mark"><span class="initials">RP</span><span class="brand">StrongDaily</span></div>
  </div>

  <nav class="nav">
    <a class="active" href="#">টাইমলাইন</a>
    <a href="#">সম্বন্ধে</a>
    <a href="#">চিত্রসম্ভার</a>
    <a href="#">পছন্দ</a>
    <a href="#">আরও ▾</a>
  </nav>

  <div class="card people"><span>লোকজন</span><span>›</span></div>
  <div class="card composer">
    <span class="tab"><span class="sq" style="background:#5b7bd5"></span>পোস্ট</span>
    <span class="tab"><span class="sq" style="border:2px solid #e58a2e"></span>ছবি/ভিডিও</span>
  </div>
</main>
</body>
</html>
```